Korrawa Tide Supply Business Cards

I need a business card design for my business. We specialise in supplying quality brand cleaning products for boats
Updates

Target Market(s)

local household people with personal boats

Industry/Entity Type

Business

Requirements
Must have
• Address - 14 Fenwick Crescent, Nickol WA 6714
Phone - 0417 382 905
Email - korrawatidesupply@mailhaven.com
Web - www.korrawatidesupply.com.au
Martin Quill
Director

Business logo is a must have
Nice to have
• Glossjet logo is optional but recommended as it shows what we do

```html
<!DOCTYPE html>
<html lang="en">
<head>
<meta charset="utf-8">
<title>Korrawa Tide Supply – Business Cards</title>
<link rel="stylesheet" href="https://fonts.googleapis.com/css2?family=Source+Sans+3:wght@300;400&family=PT+Sans+Narrow&display=swap">
<style>
  :root {
    --navy: #0d4f86;
    --orange: #f58220;
    --ink: #4a4a4a;
    --paper: #ffffff;
    --stage-light: #ffffff;
    --stage-dark: #d9d9d9;
  }
  * { margin: 0; padding: 0; box-sizing: border-box; }
  html, body { width: 1200px; height: 895px; overflow: hidden; }
  body {
    position: relative;
    background: radial-gradient(ellipse at 50% 48%, var(--stage-light) 0%, #f1f1f1 45%, var(--stage-dark) 100%);
    font-family: "Source Sans 3", sans-serif;
  }
  .card {
    position: absolute;
    width: 415px;
    height: 227px;
    border-radius: 14px;
    background: var(--paper);
    overflow: hidden;
    box-shadow: 0 3px 8px rgba(0,0,0,0.14);
  }
  .card--front-a { left: 135px; top: 129px; }
  .card--back-a  { left: 639px; top: 129px; }
  .card--front-b { left: 130px; top: 522px; }
  .card--back-b  { left: 634px; top: 522px; }

  .brand {
    position: absolute;
    color: var(--navy);
    font-weight: 400;
    text-transform: uppercase;
    text-align: center;
    line-height: 1.1;
  }
  .card--front-a .brand, .card--front-b .brand {
    left: 0; right: 0; top: 118px;
    font-size: 22px;
    letter-spacing: 4px;
  }
  .card--back-a .brand {
    left: 220px; width: 180px; top: 40px;
    font-size: 15px; letter-spacing: 2px;
  }
  .card--back-b .brand {
    left: 60px; width: 330px; top: 90px;
    font-size: 22px; letter-spacing: 4px;
  }

  .waves { position: absolute; left: 0; top: 0; width: 415px; height: 227px; }

  .holder { position: absolute; }
  .holder__name { font-weight: 300; font-size: 22px; line-height: 1; white-space: nowrap; }
  .holder__role { font-weight: 400; font-size: 9px; margin-top: 2px; text-align: right; }
  .card--back-a .holder { left: 21px; top: 47px; }
  .card--back-a .holder__name { color: var(--ink); }
  .card--back-a .holder__role { color: #777; }
  .card--back-b .holder { left: 21px; top: 26px; }
  .card--back-b .holder__name { color: var(--navy); }
  .card--back-b .holder__role { color: var(--orange); }

  .address, .contact {
    position: absolute;
    color: var(--paper);
    font-family: "PT Sans Narrow", sans-serif;
    white-space: nowrap;
  }
  .address { left: 26px; top: 196px; font-size: 11.5px; }
  .contact {
    left: 211px; top: 183px;
    padding-left: 4px;
    border-left: 1.5px solid var(--paper);
    font-size: 10px;
    line-height: 13px;
  }
  .contact .phone { font-size: 11px; margin-bottom: 3px; }
</style>
</head>
<body>

  <section class="card card--front-a">
    <div class="brand">Korrawa<br>Tide Supply</div>
  </section>

  <section class="card card--back-a">
    <div class="holder">
      <div class="holder__name">Martin Quill</div>
      <div class="holder__role">Managing Director</div>
    </div>
    <div class="brand">Korrawa Tide Supply</div>
    <svg class="waves" viewBox="0 0 415 227" aria-hidden="true">
      <path d="M0 140 C120 152 260 118 415 138 L415 227 L0 227 Z" fill="var(--navy)"/>
      <path d="M0 130 C70 134 140 138 200 135" stroke="var(--navy)" stroke-width="6" fill="none"/>
      <path d="M80 148 C200 142 300 112 415 134" stroke="var(--orange)" stroke-width="5" fill="none"/>
    </svg>
    <div class="address">14 Fenwick Crescent, Nickol WA 6714</div>
    <div class="contact">
      <div class="phone">Phone # 0417 382 905</div>
      <div>Email Id: korrawatidesupply@mailhaven.com</div>
      <div>www.korrawatidesupply.com.au</div>
    </div>
  </section>

  <section class="card card--front-b">
    <div class="brand">Korrawa<br>Tide Supply</div>
  </section>

  <section class="card card--back-b">
    <div class="holder">
      <div class="holder__name">Martin Quill</div>
      <div class="holder__role">Managing Director</div>
    </div>
    <div class="brand">Korrawa Tide Supply</div>
    <svg class="waves" viewBox="0 0 415 227" aria-hidden="true">
      <path d="M0 146 C100 150 200 122 300 128 S390 140 415 137 L415 227 L0 227 Z" fill="var(--navy)"/>
    </svg>
    <div class="address">14 Fenwick Crescent, Nickol WA 6714</div>
    <div class="contact">
      <div class="phone">Phone # 0417 382 905</div>
      <div>Email Id: korrawatidesupply@mailhaven.com</div>
      <div>www.korrawatidesupply.com.au</div>
    </div>
  </section>

</body>
</html>
```